Homemaker goats milk soap label

The name of my farm is Hollow Creek Meadow Farm. I would like to keep my label vintage 1800s is appearance. A linked to my webpage, still under development is http://pelo.trinvemar.com/dev2/fieldkinhome/. This will give you a feel for my theme. Along with other goat and bison by products, I make and sell homemade goat milk soap and I would like a special label to package my fabulous soap.
Updates

Hello Designers, To assist you with designing my label, I have attached a new photo from Lather Haven that shows the type label I am going to use.

Industry/Entity Type

Farm

```html
<!DOCTYPE html>
<html lang="en">
<head>
<meta charset="utf-8">
<title>Hollow Creek Meadow Goats Milk Soap Label</title>
<link rel="stylesheet" href="https://fonts.googleapis.com/css2?family=Marcellus&family=Rosarivo&family=Lusitana:wght@700&display=swap">
<style>
  :root {
    --paper: #fbf6b4;
    --stripe: #e2cd8c;
    --ink: #9c8563;
    --ink-dark: #8d7553;
    --art: #d9c58f;
    --frame: #c9b27e;
    --oval: #f6eba6;
    --page: #ffffff;
  }
  * { margin: 0; padding: 0; box-sizing: border-box; }
  html, body { width: 1200px; height: 939px; overflow: hidden; background: var(--page); }
  .canvas { position: relative; width: 1200px; height: 939px; }
  .label {
    position: absolute; left: 0; top: 284px; width: 1200px; height: 372px;
    background:
      linear-gradient(to bottom, rgba(251,246,180,.9) 0%, rgba(251,246,180,.55) 45%, rgba(251,246,180,.1) 100%),
      repeating-linear-gradient(90deg, var(--paper) 0 24px, var(--stripe) 24px 48px);
  }
  .ingredients-panel {
    position: absolute; left: 30px; top: 112px; width: 390px; height: 148px;
    background: linear-gradient(to bottom, var(--paper), rgba(251,246,180,.75));
  }
  .ingredients-title {
    position: absolute; left: 30px; top: 122px;
    font: 13px "Marcellus", serif; color: var(--ink);
  }
  .star-band { position: absolute; width: 392px; height: 72px; }
  .star-band svg { display: block; }
  .band-left-top { left: 30px; top: 38px; }
  .band-right-top { left: 779px; top: 38px; }
  .band-left-bottom { left: 30px; top: 260px; }
  .band-right-bottom { left: 779px; top: 260px; }
  .title-block {
    position: absolute; left: 430px; top: 6px; width: 340px; text-align: center;
    color: var(--ink);
  }
  .kicker { font: 30px "Marcellus", serif; margin-left: -60px; line-height: 44px; white-space: nowrap; }
  .farm-name { font: 31px "Rosarivo", serif; color: var(--ink-dark); line-height: 44px; white-space: nowrap; letter-spacing: -.3px; }
  .product { font: 30px "Marcellus", serif; margin-left: 60px; line-height: 38px; white-space: nowrap; }
  .emblem { position: absolute; left: 446px; top: 166px; }
  .weight {
    position: absolute; right: 28px; bottom: 8px;
    font: 700 21px "Lusitana", serif; color: var(--ink-dark); letter-spacing: .3px;
  }
</style>
</head>
<body>
<div class="canvas">
  <svg width="0" height="0" style="position:absolute">
    <defs>
      <polygon id="star" points="0,-16 4.7,-5.2 16,-5 7.3,2.4 10,14 0,7.5 -10,14 -7.3,2.4 -16,-5 -4.7,-5.2" fill="#9c8563"/>
      <g id="star-row">
        <line x1="4" y1="4" x2="388" y2="4" stroke="#9c8563" stroke-width="6" stroke-linecap="round" stroke-dasharray="0 9.1"/>
        <use href="#star" x="42" y="38"/>
        <use href="#star" x="101" y="38"/>
        <use href="#star" x="160" y="38"/>
        <use href="#star" x="219" y="38"/>
        <use href="#star" x="278" y="38"/>
        <use href="#star" x="337" y="38"/>
        <line x1="4" y1="68" x2="388" y2="68" stroke="#9c8563" stroke-width="6" stroke-linecap="round" stroke-dasharray="0 9.1"/>
      </g>
    </defs>
  </svg>

  <section class="label">
    <div class="ingredients-panel"></div>
    <p class="ingredients-title">Ingredients:</p>

    <div class="star-band band-left-top"><svg width="392" height="72"><use href="#star-row"/></svg></div>
    <div class="star-band band-right-top"><svg width="392" height="72"><use href="#star-row"/></svg></div>
    <div class="star-band band-left-bottom"><svg width="392" height="72"><use href="#star-row"/></svg></div>
    <div class="star-band band-right-bottom"><svg width="392" height="72"><use href="#star-row"/></svg></div>

    <div class="title-block">
      <p class="kicker">Home Crafted</p>
      <h1 class="farm-name">Hollow Creek Meadow</h1>
      <p class="product">Goats Milk Soap</p>
    </div>

    <svg class="emblem" width="320" height="200" viewBox="0 0 320 200">
      <ellipse cx="160" cy="104" rx="152" ry="88" fill="none" stroke="#c9b27e" stroke-width="3"/>
      <ellipse cx="160" cy="104" rx="140" ry="78" fill="#f6eba6" stroke="#c9b27e" stroke-width="1.5"/>
      <ellipse cx="160" cy="104" rx="124" ry="66" fill="#d9c58f" opacity=".75" role="img" aria-label="Engraved illustration of a goat and a bison head side by side"/>
    </svg>

    <p class="weight">nett. weight 4.5 oz</p>
  </section>
</div>
</body>
</html>
```